Billboard - Cool Garden and Landscape Company (Brand Pack Included)

NEED A PROFESSIONAL BILLBOARD TO ADVERTISE OUR BUSINESS. HAVE MOCKED UP A SAMPLE CONCEPT BUT IT REQUIRES THE ICONS TO BE DEVELOPED TO A PROFESSIONAL STANDARD (I JUST COPIED RANDOM EXAMPLES FROM THE NET)

THE ICONS REPRESENT OUR KEY PRODUCT GROUPS. (These can be redesigned)
BILLBOARD IS 6M X 3M (SEE SPEC FILE ATTACHED) - IMAGE OF THE LOCATION ADDED TO THE FILES.

BRAND GUIDE INCLUDED WITH LOGO FILES

VISIT: https://www.facebook.com/Team.Fern.Crate/
Web: www.ferncrate.co.nz

Target Market(s)

Commuter traffic - busy road - Billboard site is on the left side approx 400m before our street turn off. Age group 30+ Home owners / Builders

Industry/Entity Type

Garden Supply

Font styles to use
Other font styles liked:
• comfortaa

Requirements
Must have
• No change to our logo or brand
• Next left
• Icons for products as per mock up - note these can be redesigned
Nice to have
• Easy to see at a distance
• Clean
• Simple

```html
<!DOCTYPE html>
<html lang="en">
<head>
<meta charset="utf-8">
<title>Fern Crate Billboard</title>
<link rel="stylesheet" href="https://fonts.googleapis.com/css2?family=Montserrat:wght@700;800&family=Oswald:wght@500&display=swap">
<style>
  :root {
    --canvas-bg: #4a4a4a;
    --brand-green: #2aa14a;
    --brand-orange: #f7960d;
    --paper: #ffffff;
    --ink: #111111;
  }
  html, body {
    margin: 0;
    padding: 0;
    overflow: hidden;
  }
  .canvas {
    width: 1200px;
    height: 1200px;
    background: var(--canvas-bg);
    display: flex;
    align-items: center;
    justify-content: center;
  }
  .billboard {
    width: 1118px;
    height: 558px;
    display: block;
    box-shadow: 0 4px 10px rgba(0,0,0,0.35);
  }
  .bg-green { fill: var(--brand-green); }
  .bg-white { fill: var(--paper); }
  .accent-orange { fill: var(--brand-orange); }
  .brand-square { fill: var(--brand-green); }
  .brand-name {
    font-family: "Montserrat", sans-serif;
    font-weight: 800;
    font-size: 46px;
    fill: var(--brand-green);
    text-anchor: middle;
  }
  .product-label {
    font-family: "Oswald", sans-serif;
    font-weight: 500;
    font-size: 25px;
    fill: var(--brand-orange);
    text-anchor: middle;
  }
  .divider { stroke: var(--paper); stroke-width: 2; opacity: 0.8; }
  .icon { fill: var(--paper); }
  .icon-line { stroke: var(--paper); fill: none; stroke-width: 6; stroke-linecap: round; stroke-linejoin: round; }
  .direction-text {
    font-family: "Montserrat", sans-serif;
    font-weight: 800;
    font-size: 36px;
    fill: var(--ink);
  }
  .address-text {
    font-family: "Montserrat", sans-serif;
    font-weight: 800;
    font-size: 35px;
    fill: var(--paper);
  }
  .service-line {
    font-family: "Montserrat", sans-serif;
    font-weight: 700;
    font-size: 29px;
    fill: var(--paper);
    text-anchor: end;
  }
</style>
</head>
<body>
<main class="canvas">
  <svg class="billboard" viewBox="0 0 1118 558" xmlns="http://www.w3.org/2000/svg" aria-label="Fern Crate billboard">
    <rect class="bg-green" width="1118" height="558"/>
    <path class="accent-orange" d="M0 0 H528 C540 270 380 490 0 552 Z"/>
    <path class="bg-white" d="M0 0 H492 C500 255 340 470 0 536 Z"/>

    <g class="brand">
      <rect class="brand-square" x="176" y="110" width="96" height="96" rx="6"/>
      <text class="brand-name" x="224" y="280">FERN CRATE</text>
    </g>

    <g class="products">
      <line class="divider" x1="815" y1="60" x2="815" y2="170"/>
      <line class="divider" x1="815" y1="255" x2="815" y2="335"/>

      <g class="product-icon">
        <path class="icon" d="M668 42 C652 62 640 78 646 100 C650 112 660 118 668 118 C680 118 690 110 692 96 C694 82 684 72 680 60 C676 72 672 78 668 80 C670 66 672 54 668 42 Z"/>
        <path class="icon-line" d="M640 114 L700 130 M696 114 L636 130"/>
      </g>
      <text class="product-label" x="668" y="168">FIREWOOD</text>
      <text class="product-label" x="668" y="196">FIRE PELLETS</text>

      <g class="product-icon">
        <path class="icon-line" d="M956 125 V50"/>
        <path class="icon" d="M956 75 C940 72 930 62 928 48 C944 50 954 60 956 75 Z M956 70 C972 66 982 56 984 42 C968 44 958 54 956 70 Z M956 98 C938 95 926 84 924 70 C942 72 954 82 956 98 Z M956 92 C974 88 986 78 988 64 C970 66 958 76 956 92 Z"/>
        <path class="icon" d="M906 128 C920 112 940 110 956 116 C972 110 994 112 1006 128 Z"/>
      </g>
      <text class="product-label" x="956" y="168">COMPOST</text>
      <text class="product-label" x="956" y="196">SOIL + MULCH</text>

      <g class="product-icon">
        <ellipse class="icon" cx="670" cy="225" rx="12" ry="10"/>
        <ellipse class="icon" cx="664" cy="250" rx="22" ry="13"/>
        <ellipse class="icon" cx="670" cy="282" rx="36" ry="17"/>
      </g>
      <text class="product-label" x="668" y="334">DECORATIVE STONE</text>
      <text class="product-label" x="668" y="360">AGGREGATES</text>

      <g class="product-icon">
        <rect class="icon" x="936" y="232" width="88" height="32"/>
        <path class="icon-line" d="M936 262 H896 M902 254 V286"/>
        <circle class="icon" cx="985" cy="276" r="15"/>
        <circle fill="var(--brand-green)" cx="985" cy="276" r="6"/>
      </g>
      <text class="product-label" x="956" y="334">HIRE TRAILERS</text>
      <text class="product-label" x="956" y="360">DELIVERY</text>
    </g>

    <polygon class="accent-orange" points="40,445 95,390 95,420 350,420 350,470 95,470 95,500"/>
    <text class="direction-text" x="100" y="459">NEXT LEFT</text>

    <rect class="accent-orange" x="360" y="413" width="758" height="62"/>
    <text class="address-text" x="393" y="458">42 FERRIS ROAD (OFF KETTERING)</text>
    <text class="service-line" x="1032" y="507">Garden &amp; Landscape Supplies</text>
  </svg>
</main>
</body>
</html>
```